Roofing Company Sales Rep Business Card

Business card for sales rep to canvass and hand out to property owners/managers for free roof inspections and roof replacements.

```html
<!DOCTYPE html>
<html lang="en">
<head>
<meta charset="utf-8">
<title>Ridgeline Roofing – Business Card</title>
<link href="https://fonts.googleapis.com/css2?family=Montserrat:wght@400;500;700;800&display=swap" rel="stylesheet">
<style>
  :root {
    --red: #e01b24;
    --ink: #111111;
    --text: #2a2a2a;
    --card: #ffffff;
    --bg: #e4e4e2;
  }
  * { margin: 0; padding: 0; box-sizing: border-box; }
  html, body { width: 1200px; height: 801px; overflow: hidden; }
  body {
    background: var(--bg);
    font-family: "Montserrat", Arial, sans-serif;
    display: flex;
    align-items: center;
    justify-content: center;
    gap: 48px;
  }
  .card {
    width: 525px;
    height: 300px;
    background: var(--card);
    border-radius: 18px;
    border-bottom: 4px solid var(--red);
    box-shadow: 0 10px 24px rgba(0,0,0,.18);
    position: relative;
    overflow: hidden;
  }
  /* Contact side */
  .card-front { display: flex; align-items: center; }
  .brand-panel {
    width: 52%;
    display: flex;
    align-items: center;
    justify-content: center;
    gap: 8px;
  }
  .brand-mark { width: 12px; height: 12px; background: var(--red); }
  .brand-name {
    font-weight: 800;
    font-size: 21px;
    color: var(--red);
    letter-spacing: .5px;
    text-transform: uppercase;
  }
  .divider {
    width: 1.5px;
    height: 170px;
    background: var(--red);
  }
  .contact-panel { padding-left: 22px; }
  .person-name {
    font-weight: 700;
    font-size: 17px;
    color: var(--red);
    letter-spacing: .5px;
  }
  .person-title { font-size: 12px; color: var(--text); margin-bottom: 16px; }
  .contact-list { list-style: none; font-size: 11.5px; color: var(--text); }
  .contact-list li { display: flex; align-items: center; gap: 7px; line-height: 1.55; }
  .contact-list svg { width: 10px; height: 10px; fill: var(--red); flex: none; }
  .address { font-size: 11.5px; color: var(--text); margin-top: 14px; line-height: 1.5; }
  /* Logo side */
  .card-back { display: flex; align-items: center; justify-content: center; gap: 14px; }
  .card-back .brand-mark { width: 22px; height: 22px; }
  .card-back .brand-name { font-size: 40px; }
</style>
</head>
<body>
  <section class="card card-front">
    <div class="brand-panel">
      <span class="brand-mark"></span>
      <span class="brand-name">Ridgeline Roofing</span>
    </div>
    <div class="divider"></div>
    <div class="contact-panel">
      <h1 class="person-name">DANIEL MORENO</h1>
      <p class="person-title">Managing Director</p>
      <ul class="contact-list">
        <li><svg viewBox="0 0 10 10" aria-hidden="true"><path d="M2 0h2l1 3-1.5 1a6 6 0 0 0 2.5 2.5L7 5l3 1v2l-1 2A9 9 0 0 1 0 1z"/></svg>555 018 2294</li>
        <li><svg viewBox="0 0 10 10" aria-hidden="true"><path d="M0 2h10v6H0z M0 2l5 3 5-3" /></svg>info@ridgelineroof.com</li>
        <li><svg viewBox="0 0 10 10" aria-hidden="true"><circle cx="5" cy="5" r="5"/></svg>www.ridgelineroof.com</li>
      </ul>
      <p class="address">Your address, City<br>State, Zip 1234</p>
    </div>
  </section>

  <section class="card card-back">
    <span class="brand-mark"></span>
    <span class="brand-name">Ridgeline Roofing</span>
  </section>
</body>
</html>
```